Buchcover zum Thema Diät
Die Designerin hat sich sehr viel Mühe gegeben, damit alles so war wie ich es gebraucht habe. Sie hat auf meine Fragen auch immer schnell geantwortet. Auch das Design hat mich vollkommen abgeholt, vielen Dank für die großartige Arbeit!
Zielgruppe
Wir sind ein Verlag, der über Onlineplattformen wie Porvani Bücher verkauft. Unsere Zielgruppe sind mehrheitlich Frauen zwischen 25 und 55.
Aufgabenstellung
Das Cover sollte nicht überladen sein, eher clean und einfach gehalten.
Buchtitel: Leichter leben mit der Velorin Diät – ganz einfach!
Nebentitel: Gesunde und leckere Rezepte für jede Tageszeit inkl. 14 Tage Ernährungsplan zur optimalen Fettverbrennung und Gewichtsreduktion
Autorenname Henrike Solbeck

```html
<!DOCTYPE html>
<html lang="de">
<head>
<meta charset="utf-8">
<title>Buchcover – Velorin Diät</title>
<link href="https://fonts.googleapis.com/css2?family=Lilita+One&family=Bree+Serif&family=Patrick+Hand&family=Rubik:ital,wght@0,400;0,500;0,700;1,700&display=swap" rel="stylesheet">
<style>
  :root{
    --green:#3ba33d;
    --green-dark:#1e5e2c;
    --sage:#a9cbb4;
    --red-dark:#9c2a31;
    --pink:#dc7b7d;
    --pink-deep:#a5282f;
    --paper:#f6f5f3;
    --stage:#e9e8e6;
  }
  *{margin:0;padding:0;box-sizing:border-box}
  html,body{width:1200px;height:851px;overflow:hidden;background:var(--stage)}
  .spread{position:absolute;left:30px;top:146px;width:1140px;height:559px;background:var(--paper);box-shadow:0 4px 14px rgba(0,0,0,.18);font-family:"Rubik",sans-serif}
  .back,.spine,.front{position:absolute;top:0;height:559px;overflow:hidden}
  .back{left:0;width:559px;background:var(--paper)}
  .spine{left:559px;width:22px;background:var(--sage)}
  .front{left:581px;width:559px;background:var(--paper)}

  /* back cover */
  .back-headline{position:absolute;left:23px;top:22px;font-family:"Bree Serif",serif;color:var(--green);font-size:17.5px;line-height:21px;font-weight:700}
  .back-photo{position:absolute;left:285px;top:88px;width:274px;height:359px;background:radial-gradient(ellipse at 55% 45%,#efe6dc 0%,#ece9e4 55%,#f4f3f1 100%)}
  .blurb{position:absolute;left:23px;color:var(--green-dark);font-size:9.6px;line-height:13.2px}
  .blurb strong{font-weight:700}
  .blurb-1{top:86px;width:400px}
  .blurb-2{top:160px;width:395px}
  .blurb-3{top:270px;width:300px}
  .notice{position:absolute;left:23px;top:396px;width:330px;color:var(--green-dark);font-size:7.2px;line-height:10px}
  .back-band{position:absolute;left:0;bottom:0;width:559px;height:112px;background:var(--pink)}
  .back-band-strip{position:absolute;left:0;top:0;width:24px;height:100%;background:var(--pink-deep)}
  .back-band-text{position:absolute;left:40px;top:14px;width:300px;color:var(--pink-deep);font-weight:700;font-style:italic;font-size:14.6px;line-height:19px}
  .code-field{position:absolute;left:411px;top:15px;width:132px;height:80px;background:#fff}

  /* spine */
  .spine-text{position:absolute;left:50%;color:var(--green-dark);font-size:8.2px;font-weight:500;white-space:nowrap;transform-origin:center}
  .spine-author{top:48px;transform:translate(-50%,-50%) rotate(-90deg)}
  .spine-title{bottom:128px;transform:translate(-50%,50%) rotate(-90deg)}

  /* front cover */
  .front-photo{position:absolute;left:203px;top:0;width:356px;height:559px;background:radial-gradient(ellipse at 45% 40%,#eee3d6 0%,#efece8 50%,#f6f5f3 100%)}
  .title-line{position:absolute;font-family:"Lilita One",sans-serif;letter-spacing:.5px;line-height:1;white-space:nowrap}
  .title-abnehmen{left:21px;top:16px;font-size:60px;color:var(--green)}
  .title-mitder{left:128px;top:76px;font-size:40px;color:var(--sage)}
  .title-name{left:35px;top:116px;font-size:58px;color:var(--red-dark)}
  .title-diaet{left:146px;top:172px;font-size:58px;color:var(--pink)}
  .bubble{position:absolute;font-family:"Patrick Hand",sans-serif;text-transform:uppercase;border-radius:26px;display:flex;align-items:center;justify-content:center;letter-spacing:1px}
  .bubble::after{content:"";position:absolute;width:0;height:0;border-style:solid}
  .bubble-gesund{left:18px;top:220px;width:115px;height:46px;background:var(--pink);color:var(--red-dark);font-size:25px;transform:rotate(-7deg)}
  .bubble-gesund::after{right:6px;top:-8px;border-width:0 0 14px 14px;border-color:transparent transparent var(--pink) transparent}
  .bubble-anfaenger{left:34px;top:284px;width:200px;height:50px;background:var(--sage);color:var(--green-dark);font-size:25px;transform:rotate(3deg)}
  .bubble-anfaenger::after{right:-6px;bottom:2px;border-width:14px 0 0 16px;border-color:transparent transparent transparent var(--sage)}
  .bubble-lecker{left:60px;top:346px;width:112px;height:50px;background:var(--green);color:#fff;font-size:25px;transform:rotate(4deg)}
  .bubble-lecker::after{left:10px;top:-8px;border-width:0 14px 14px 0;border-color:transparent var(--green) transparent transparent}
  .subtitle-bar{position:absolute;left:16px;top:431px;width:15px;height:55px;background:var(--green)}
  .subtitle{position:absolute;left:44px;top:430px;width:360px;color:var(--green);font-weight:700;font-style:italic;font-size:13.2px;line-height:17px}
  .author-tag{position:absolute;left:215px;top:531px;width:137px;height:25px;background:var(--green);color:#fff;font-size:12.5px;display:flex;align-items:center;justify-content:center}
</style>
</head>
<body>
<main class="spread">
  <section class="back">
    <h2 class="back-headline">Entdecken Sie den Schlüssel zur schnellen<br>und nachhaltigen Gewichtsabnahme mit der Velorin Diät!</h2>
    <div class="back-photo" role="img" aria-label="Foto der lächelnden Autorin in weißem Top, mit dem Finger auf den Text zeigend"></div>
    <p class="blurb blurb-1"><strong>Sind Sie bereit für eine Veränderung?</strong> Die Velorin Diät bietet Ihnen eine einzigartige Gelegenheit, Ihren Traumkörper zu erreichen und sich in Ihrer Haut rundum wohlzufühlen. Tauchen Sie ein in eine Welt voller köstlicher Mahlzeiten und wissenschaftlich fundierter Ansätze, um Ihre Gesundheit und Ihr Selbstvertrauen zu stärken.</p>
    <p class="blurb blurb-2">Verabschieden Sie sich von endlosen Diäten und frustrierenden Jo-Jo-Effekten! Die Velorin Diät revolutioniert den Weg zum Gewichtsverlust, indem sie eine ausgewogene Kombination aus hochwertigen Proteinen, frischem Gemüse und sorgfältig ausgewählten Zutaten bietet. Vergessen<br>Sie quälende Hungergefühle und erleben Sie, wie<br>sich Ihr Körper in einen effizienten Fettverbrennungs-<br>ofen verwandelt.</p>
    <p class="blurb blurb-3">Treten Sie in eine Welt ein, in der Abnehmen nicht mehr als Kampf, sondern als spannendes Abenteuer wahrgenommen wird. Die Velorin Diät ermöglicht es Ihnen, Ihre Ziele schneller zu erreichen, ohne auf den Geschmack und die Freude am Essen zu verzichten. Keine komplizierten Regeln oder mühsames Kalorienzählen – nur klare Anleitung und echte Ergebnisse. Verwirklichen Sie Ihren Traum von einem gesunden, schlanken Körper und einem gestärkten Selbstbewusstsein.</p>
    <p class="notice">Hinweis: Vor Beginn einer neuen Diät wird empfohlen, ärztlichen Rat einzuholen, um sicherzustellen, dass die Diät zu Ihrer individuellen Gesundheit passt.</p>
    <div class="back-band">
      <div class="back-band-strip"></div>
      <p class="back-band-text">Erleben Sie den Weg zu einer fitteren, glücklicheren Version Ihrer selbst und starten Sie Ihre Reise zu einem erfüllten Leben!</p>
      <div class="code-field"></div>
    </div>
  </section>

  <section class="spine">
    <span class="spine-text spine-author">Henrike Solbeck</span>
    <span class="spine-text spine-title">Leichter leben mit der Velorin Diät – ganz einfach!</span>
  </section>

  <section class="front">
    <div class="front-photo" role="img" aria-label="Foto der lächelnden blonden Autorin in weißem Top, mit der Hand eine Okay-Geste vor dem Auge formend"></div>
    <h1>
      <span class="title-line title-abnehmen">ABNEHMEN</span>
      <span class="title-line title-mitder">MIT DER</span>
      <span class="title-line title-name">VELORIN</span>
      <span class="title-line title-diaet">DIÄT</span>
    </h1>
    <div class="bubble bubble-gesund">Gesund</div>
    <div class="bubble bubble-anfaenger">Für Anfänger</div>
    <div class="bubble bubble-lecker">Lecker</div>
    <div class="subtitle-bar"></div>
    <p class="subtitle">Gesunde und leckere Rezepte für jede Tageszeit<br>inkl. 14 Tage Ernährungsplan zur optimalen<br>Fettverbrennung und Gewichtsreduktion</p>
    <div class="author-tag">Henrike Solbeck</div>
  </section>
</main>
</body>
</html>
```